The Quiet Ascent Book Cover

Book Title:
The Quiet Ascent: Lessons of Insight From A Circle of Mentors to Guide You Toward a Fuller Journey

This book will offer the wisdom and philosophies of a variety of different coaches to allow future clients to get a taste of you and your style and prepare them to work with you!

A coach does not fix you. Or heal you. They coach you - offer thoughts to ponder, guidance, techniques to try. All to help you plays and succeed at the game of life.

Each coach has their own personality, training, experience, method and philosophy they bring to the table. The underlying purpose is to guide you through The Quiet Ascent, to become the person you desire and aspire to be. Different coaches for different folks, yet they all have their own unique wisdom and special sauce to share.

This book is a collection of just that. A tasting of the wisdom and philosophies of a variety of different coaches for you to experience.

Types of Coaches: Clarity, Dreams, Goals, Motivation, Mindset,  Subconscious, Beliefs, Behavior, Accountability, Life, Wellness, Love & Dating, Relationships, Sex, Business, Career,  Executive,  Personal Development,  Writing, Wellness, Fitness, Parenting,  Style, Spirituality, Public Speaking, Financial,  Time management, Weight Loss, Running, Self esteem,  Tarot, Astrology, Enneagram, Soul path/ Dharma, Skills, Performance,  Speaking / Communication, Leadership, Shadow Work, Acting, Sports, ANY & ALL

Target Market(s)

Males or females looking for guidance and words of wisdom from an expert coach - maybe to find one that resonates with them to work with further. Ages 16 and up. Any Gender. International. Looking to improve their life!

Industry/Entity Type

Self Development, Wellness, Coaching, Personal Growth, Fitness, Spirituality, Business, Relationships

Font styles to use
Serif
Script

Colors
0054AA
0677BA
7BADD7
CADEEF
E8F1F8
FFF300
FFF600
FEFA6F
FFFEC7
FFFEE8

Requirements
Must have
• I am looking for a visually appealing, unique cover that encompasses the breadth and depth of the transformation that people can go through and inspires them to want to grow and change even more. I love when elegant and classic simplicity is combined with some kind of twist that catches the eye and provokes thought. I love complimentary fonts, colors, design elements. You can visit my Veltrano Author Page - Dr. Marisol Penbury Aldane to see my titles to see what I have liked! But I am also excited to see where you can make my vision even better!!
Nice to have
• Front Cover - Image, Title and Subtitle, The Lark Publishing House, Spine - Title and Publishing House Logo, Back - Book Blurb, Authors Names, Info about Publishing House, ISBN Barcode
Should not have
• Anything too feminine or too masculine as I want to encourage coaches of all genders to participate.

```html
<!DOCTYPE html>
<html lang="en">
<head>
<meta charset="utf-8">
<title>The Quiet Ascent — Book Cover</title>
<link rel="stylesheet" href="https://fonts.googleapis.com/css2?family=Montserrat:wght@800&family=Poppins:wght@500&family=Open+Sans:wght@400&display=swap">
<style>
  :root {
    --stage: #404040;
    --paper: #f3f3f5;
    --ink: #333333;
    --ink-soft: #5f5f5f;
    --art-green: #9fd488;
    --art-yellow: #f6dc86;
    --art-orange: #f7c98a;
    --art-blue: #a9c3e8;
    --art-purple: #d3a6d6;
  }
  * { margin: 0; padding: 0; box-sizing: border-box; }
  html, body {
    width: 1200px; height: 1000px; overflow: hidden;
    background: var(--stage);
  }
  .cover {
    position: absolute; left: 384px; top: 176px;
    width: 432px; height: 648px;
    background: var(--paper);
    overflow: hidden;
  }
  .cover-art {
    position: absolute; inset: 0;
    background:
      radial-gradient(ellipse 36% 30% at 50% 48%, var(--art-green) 0%, rgba(159,212,136,0.6) 45%, rgba(243,243,245,0) 100%),
      radial-gradient(ellipse 60% 50% at 50% 48%, rgba(247,201,138,0.55) 0%, rgba(246,220,134,0.35) 50%, rgba(243,243,245,0) 100%),
      radial-gradient(ellipse 75% 62% at 50% 48%, rgba(169,195,232,0.45) 0%, rgba(211,166,214,0.25) 60%, rgba(243,243,245,0) 100%),
      var(--paper);
  }
  .title {
    position: absolute; left: 30px; top: 38px; width: 374px;
    color: var(--ink);
  }
  .title-main {
    display: block; width: 374px; height: 46px;
    font-family: "Montserrat", sans-serif; font-weight: 800;
  }
  .title-main text { fill: var(--ink); }
  .title-sub {
    display: block; text-align: right;
    font-family: "Poppins", sans-serif; font-weight: 500;
    font-size: 22px; line-height: 1; letter-spacing: 5px;
    margin-top: 2px; margin-right: -5px;
  }
  .subtitle {
    position: absolute; left: 0; top: 524px; width: 432px;
    text-align: center;
    font-family: "Poppins", sans-serif; font-weight: 500;
    font-size: 13.5px; line-height: 17px; letter-spacing: 0.6px;
    color: var(--ink-soft);
  }
  .publisher {
    position: absolute; left: 0; top: 596px; width: 432px;
    text-align: center;
    font-family: "Open Sans", sans-serif; font-weight: 400;
    font-size: 19px; letter-spacing: 0.5px;
    color: var(--ink-soft);
  }
</style>
</head>
<body>
  <main class="cover">
    <div class="cover-art" role="img"
         aria-label="Illustration: multicoloured sunburst rays radiating across the cover around a swirl of green caterpillars, chrysalises and five colourful butterflies"></div>

    <h1 class="title">
      <svg class="title-main" viewBox="0 0 374 46" aria-label="The Quiet">
        <text x="0" y="0" font-size="10" letter-spacing="1" transform="translate(9 40) rotate(-90)">THE</text>
        <text x="14" y="40" font-size="46" textLength="358" lengthAdjust="spacing">QUIET</text>
      </svg>
      <span class="title-sub">ASCENT</span>
    </h1>

    <p class="subtitle">Lessons of Insight From<br>A Circle of Mentors to Guide You<br>Toward a Fuller Journey</p>

    <p class="publisher">THE LARK PUBLISHING HOUSE</p>
  </main>
</body>
</html>
```